Warren D Pellham New Business Card Design

I assist families or individuals with downsizing. When they need to sell estate items I manage the process. I may buy their items. I may place their items with auction houses or I may bring in a variety of experts to sell all of the items. We help clients sell a huge variety of items including art, jewelry, coins, watches, antiques, collectibles, etc.

Target Market(s)

Two markets...One market is the clients I serve which are usually seniors or their family. These are individuals that need to sell on item or a house full if they estate is being liquidated. The other market is those that refer clients to me. Real Estate professionals, active senior communities, trust and estate lawyers and financial advisors.

Contact Information for Business Card

This is a new business so we do not have a logo. We may not need a logo. Feel free to visit our website at www.warrendpellham-example.com for more information on the service we provide. I am a private consultant so my name needs to be prominent. My name is my brand. We need the card to let people know how to contact us via phone, website and email. Easy to read. Many of our clients are elderly.

Font styles to use
Sans Serif

Requirements
Must have
• My name. Our contact information.
• Warren D Pellham
• 555-218-7034 Office
• 555-639-1582 Cell
• info@warrendpellham-example.com
• www.warrendpellham-example.com

```html
<!DOCTYPE html>
<html lang="en">
<head>
<meta charset="utf-8">
<title>Warren D Pellham – Business Card</title>
<link rel="stylesheet" href="https://fonts.googleapis.com/css2?family=Roboto:wght@500;700&display=swap">
<style>
  :root {
    --stage-top: #7b7b7b;
    --stage-bottom: #636363;
    --white: #ffffff;
    --ink: #151515;
    --gold: #a8762c;
    --tan-deep: #ad8231;
    --tan-mid: #d9c29a;
    --wood-dark: #2a1609;
    --wood-mid: #5a3117;
    --wood-light: #8a5428;
    --suit: #1e1c1c;
  }
  * { margin: 0; padding: 0; box-sizing: border-box; }
  html, body { width: 1200px; height: 566px; overflow: hidden; }
  body {
    position: relative;
    font-family: "Roboto", Arial, sans-serif;
    background: linear-gradient(180deg, var(--stage-top) 0%, var(--stage-bottom) 100%);
  }

  .card { position: absolute; overflow: hidden; }

  /* Front side */
  .card-front { left: 68px; top: 30px; width: 505px; height: 288px; }
  .front-photo {
    position: absolute; inset: 0;
    background:
      radial-gradient(ellipse 90px 200px at 80px 190px, var(--suit) 0%, var(--suit) 60%, transparent 100%),
      linear-gradient(90deg, var(--wood-dark) 0%, var(--wood-mid) 35%, var(--wood-light) 60%, var(--wood-mid) 85%, var(--wood-dark) 100%);
  }
  .front-text {
    position: absolute; left: 150px; right: 0; top: 93px;
    text-align: center; color: var(--white);
    text-shadow: 0 1px 3px rgba(0,0,0,.75);
  }
  .front-name { font-size: 29px; font-weight: 700; letter-spacing: .3px; line-height: 34px; }
  .front-role { margin-top: 14px; font-size: 18px; font-weight: 700; line-height: 23px; }

  /* Back side */
  .card-back {
    left: 621px; top: 28px; width: 485px; height: 293px;
    background: linear-gradient(180deg, var(--white) 0%, var(--tan-mid) 52%, var(--tan-deep) 100%);
  }
  .back-name {
    position: absolute; left: 0; right: 0; top: 66px; text-align: center;
    color: var(--gold); font-size: 25px; font-weight: 700; letter-spacing: .3px;
  }
  .back-role {
    position: absolute; left: 0; right: 0; top: 102px; text-align: center;
    color: var(--ink); font-size: 14.5px; font-weight: 700; letter-spacing: .2px;
  }
  .contact-list { position: absolute; left: 28px; top: 192px; list-style: none; }
  .contact-item {
    display: flex; align-items: center; height: 19px;
    color: var(--ink); font-size: 12px; font-weight: 700;
  }
  .contact-icon { width: 10px; height: 10px; margin-right: 9px; flex: none; }
  .consult-call {
    position: absolute; right: 28px; top: 237px; width: 140px;
    text-align: center; color: var(--white);
    font-size: 11px; font-weight: 700; line-height: 14px;
  }
</style>
</head>
<body>

<section class="card card-front">
  <div class="front-photo" role="img" aria-label="Portrait photograph of the consultant standing with arms crossed in front of wooden bookshelves"></div>
  <div class="front-text">
    <h1 class="front-name">WARREN D PELLHAM</h1>
    <p class="front-role">COLLECTIBLE ASSET BUYER<br>BROKER &amp; CONSULTANT</p>
  </div>
</section>

<section class="card card-back">
  <h2 class="back-name">WARREN D PELLHAM</h2>
  <p class="back-role">COLLECTIBLE ASSET BUYER , BROKER &amp; CONSULTANT</p>

  <ul class="contact-list">
    <li class="contact-item">
      <svg class="contact-icon" viewBox="0 0 10 10"><rect x="2.5" y="0.5" width="5" height="9" rx="1" fill="none" stroke="#fff" stroke-width="1"/></svg>
      555-639-1582
    </li>
    <li class="contact-item">
      <svg class="contact-icon" viewBox="0 0 10 10"><path d="M1 4 Q5 0 9 4 L7.5 5 L6.5 3.5 L3.5 3.5 L2.5 5 Z" fill="#fff"/><rect x="2" y="5.5" width="6" height="3.5" fill="#fff"/></svg>
      555-218-7034
    </li>
    <li class="contact-item">
      <svg class="contact-icon" viewBox="0 0 10 10"><rect x="1" y="2.5" width="8" height="5.5" fill="#fff"/><path d="M1 2.5 L5 5.5 L9 2.5" fill="none" stroke="#b0874a" stroke-width=".8"/></svg>
      info@warrendpellham-example.com
    </li>
    <li class="contact-item">
      <svg class="contact-icon" viewBox="0 0 10 10"><circle cx="5" cy="5" r="4" fill="none" stroke="#fff" stroke-width="1.2"/><path d="M5 2.5 V5 H7" fill="none" stroke="#fff" stroke-width="1"/></svg>
      www.warrendpellham-example.com
    </li>
  </ul>

  <p class="consult-call">CALL FOR<br>A FREE CONSULTATION</p>
</section>

</body>
</html>
```